We are looking for a simple design that would be uplifting for
upscale drug addicts

MERIDIAN CIRCLE

PLEASE SEE THE LINK FOR TAG LINE AND CONTENT

thank you.

here is all the actual info we need and we want something like this...

http://assets.qlm.brivostore.com/rest/items/7c2910e5b337de81f94a02bd57e644163ab9fe0a6712?uid=bd31c9e2f7a04c18b6e0d44721fa93c5%2fdrafts&expires=1408211537&signature=kTp4WmQxNvLzHa8YbEoRcJsGf2B%3d

The shape and colors don't have to be like what I posted it is only an example.

Target Market(s)

Wall Street, internet and creative types, men, early 30's,
upwardly mobile, drug addicts

current site

bkltornavel.com

now launching new name Meridian Circle

Industry/Entity Type

Drug

Requirements
Must have
• upscale look, great font
Should not have
• a corporate look but should not look like a clinic.

```html
<!DOCTYPE html>
<html lang="en">
<head>
<meta charset="utf-8">
<title>Meridian Circle – Business Card</title>
<link href="https://fonts.googleapis.com/css2?family=Roboto:wght@300;400;500&display=swap" rel="stylesheet">
<style>
  :root {
    --page-top: #f4f5f5;
    --page-bottom: #dcdedf;
    --card-frame: #c9cacb;
    --card-dark: #3b3b3d;
    --card-dark-edge: #333335;
    --accent: #2499cf;
    --accent-deep: #1b7fae;
    --ribbon-shadow: #9a9b9d;
    --text-light: #e6e6e6;
    --text-muted: #cfcfcf;
  }
  * { margin: 0; padding: 0; box-sizing: border-box; }
  html, body { width: 1200px; height: 900px; overflow: hidden; }
  body {
    background: radial-gradient(ellipse at 50% 45%, var(--page-top) 0%, var(--page-bottom) 100%);
    font-family: "Roboto", Arial, sans-serif;
    position: relative;
  }
  .card-frame {
    position: absolute;
    left: 136px; top: 192px;
    width: 928px; height: 516px;
    background: var(--card-frame);
    padding: 14px;
    box-shadow: 0 22px 26px -18px rgba(0,0,0,.55);
  }
  .card {
    position: relative;
    width: 100%; height: 100%;
    background: linear-gradient(160deg, #434345 0%, var(--card-dark) 45%, var(--card-dark-edge) 100%);
    overflow: hidden;
    color: var(--text-light);
  }
  .brand-name {
    position: absolute;
    left: 20px; top: 22px;
    font-size: 43px; font-weight: 500;
    letter-spacing: -1px;
    color: var(--text-light);
  }
  .brand-rule {
    position: absolute;
    left: 0; right: 0; top: 84px;
    border-top: 2px dashed var(--accent);
  }
  .tagline {
    position: absolute;
    left: 20px; top: 96px;
    font-size: 14px; font-weight: 400;
    color: var(--text-muted);
  }
  .name-ribbon {
    position: absolute;
    left: 454px; top: 160px;
    width: 446px; height: 140px;
  }
  .person {
    position: absolute;
    right: 52px; top: 190px;
    text-align: right;
  }
  .person-name { font-size: 36px; font-weight: 400; color: #fff; line-height: 1.1; }
  .person-role { font-size: 20px; font-weight: 400; color: #eef6fb; margin-top: 4px; }
  .contact {
    position: absolute;
    left: 50px; top: 354px;
    font-size: 21px; font-weight: 300;
    color: var(--text-muted);
  }
  .contact-row { display: flex; align-items: center; gap: 14px; }
  .contact-row + .contact-row { margin-top: 12px; }
  .contact-icon { width: 32px; height: 32px; flex: none; }
  .phones { line-height: 1.15; }
  .phones span { display: block; }
  .phones span + span { padding-left: 3px; }
  .divider {
    position: absolute;
    left: 492px; top: 372px;
    width: 2px; height: 112px;
    background: var(--accent-deep);
  }
  .address {
    position: absolute;
    left: 540px; top: 386px;
    font-size: 25px; font-weight: 300;
    line-height: 1.33;
    color: var(--text-muted);
  }
</style>
</head>
<body>
  <div class="card-frame">
    <div class="card">
      <div class="brand-name">MERIDIAN CIRCLE</div>
      <div class="brand-rule"></div>
      <p class="tagline">We don't cut any corners when it comes to your longterm recovery</p>

      <svg class="name-ribbon" viewBox="0 0 446 140" aria-hidden="true">
        <polygon points="4,28 410,28 446,6 446,94 416,118 0,118" fill="var(--ribbon-shadow)"/>
        <polygon points="14,20 404,20 446,0 446,86 408,104 10,104" fill="var(--accent)"/>
        <polygon points="404,20 446,0 446,12 410,28" fill="var(--accent-deep)"/>
      </svg>
      <div class="person">
        <div class="person-name">Daniel Varrow, CASAC</div>
        <div class="person-role">Program Coordinator</div>
      </div>

      <div class="contact">
        <div class="contact-row">
          <svg class="contact-icon" viewBox="0 0 32 32" aria-hidden="true">
            <circle cx="16" cy="16" r="14" fill="none" stroke="var(--accent)" stroke-width="2.2"/>
            <path d="M11 8.5c1.2-.8 2.3-.4 3 .8l1.2 2.2c.5 1 .2 1.8-.6 2.4l-.9.7c.9 2 2.3 3.6 4.2 4.7l.8-.8c.7-.7 1.6-.8 2.4-.2l2 1.4c1 .7 1.2 1.8.3 2.8-1.6 1.8-3.8 1.8-6.3.3-3.6-2.2-6.4-5.8-7.3-9.4-.5-2.1 0-3.9 1.2-4.9z" fill="none" stroke="var(--accent)" stroke-width="1.8" stroke-linejoin="round"/>
          </svg>
          <div class="phones"><span>212.555.0147</span><span>212.555.0148</span></div>
        </div>
        <div class="contact-row">
          <svg class="contact-icon" viewBox="0 0 32 32" aria-hidden="true">
            <circle cx="16" cy="16" r="14" fill="none" stroke="var(--accent)" stroke-width="2.2"/>
            <path d="M8 22V11l8 8 8-8v11" fill="none" stroke="var(--accent)" stroke-width="2.2" stroke-linejoin="round"/>
          </svg>
          <span>counselor@harborlinewell.com</span>
        </div>
      </div>

      <div class="divider"></div>
      <div class="address">418 W. 52nd St. Suite 302<br>New York, NY 10019</div>
    </div>
  </div>
</body>
</html>
```